Hudson Crest IT Service, Technology & Security Co.

need a new business card design for our Technology & Security Company. We are a Computer Networking Company, Security Camera Installers, Phone Systems.

Target Market(s)

Construction, Medical, Law Offices, Accounting, Retail etc.

Industry/Entity Type

Information Technology

Logo is attached, colors are Blue, Red, Black. Blue for Technology & Red is for Security Cameras, Access Control, Alarm Systems

Colors
fbed22
ec1f27
0555a3
ffffff

Requirements
Must have
• Pictures or Icons for
• For Technology:
• Computer, Network, Phone System, Copier, TV, Cabling
• For Security:
• Video Surveillance, Access Control, Intercom, Fire Alarm, Burglar Alarm, Time Clock

```html
<!DOCTYPE html>
<html lang="en">
<head>
<meta charset="utf-8">
<title>Hudson Crest IT Service – Business Card</title>
<link rel="stylesheet" href="https://fonts.googleapis.com/css2?family=Montserrat:wght@800&family=Open+Sans:wght@400;600&display=swap">
<style>
  :root {
    --brand-blue: #0555a3;
    --brand-red: #ec1f27;
    --ink: #222222;
    --paper: #ffffff;
    --paper-shade: #ececec;
    --card-black: #050505;
    --stage: #5a5a5a;
  }
  * { box-sizing: border-box; margin: 0; padding: 0; }
  html, body {
    width: 1200px; height: 904px; overflow: hidden;
    background: var(--stage);
    font-family: "Open Sans", Arial, sans-serif;
  }
  .sheet {
    width: 1200px; height: 904px;
    display: flex; flex-direction: column; align-items: center; justify-content: center;
    gap: 40px;
  }
  .card {
    position: relative;
    width: 720px; height: 412px;
    box-shadow: 0 10px 24px rgba(0,0,0,.35);
    overflow: hidden;
  }

  /* Wordmark */
  .wordmark {
    display: flex; align-items: center; gap: 12px;
    font-family: "Montserrat", Arial, sans-serif;
    font-weight: 800; font-size: 34px; letter-spacing: -0.5px;
    white-space: nowrap;
  }
  .wordmark__dot { width: 16px; height: 16px; border-radius: 50%; background: var(--brand-red); }

  /* Back */
  .card--back { background: var(--card-black); color: var(--paper); text-align: center; }
  .card--back .wordmark { position: absolute; top: 112px; left: 0; right: 0; justify-content: center; color: var(--paper); }
  .services { position: absolute; top: 218px; left: 0; right: 0; font-size: 17px; line-height: 1.45; }
  .services__heading { font-weight: 600; }
  .services__heading--tech { color: var(--brand-blue); }
  .services__heading--security { color: var(--brand-red); }

  /* Front */
  .card--front { background: linear-gradient(160deg, var(--paper) 0%, var(--paper-shade) 100%); color: var(--ink); }
  .card--front .wordmark { position: absolute; top: 96px; left: 0; right: 0; justify-content: center; color: var(--ink); }
  .holder { position: absolute; top: 236px; right: 400px; text-align: right; }
  .holder__name { color: var(--brand-blue); font-weight: 600; font-size: 26px; line-height: 1.1; }
  .holder__role { font-size: 17px; }
  .divider { position: absolute; top: 196px; left: 340px; width: 1.5px; height: 112px; background: var(--ink); }
  .contact { position: absolute; top: 192px; left: 362px; font-size: 16px; line-height: 1.35; }
  .contact__address { margin-bottom: 12px; }
  .contact__row { display: flex; align-items: center; gap: 10px; }
  .contact__row svg { width: 14px; height: 14px; flex: none; fill: var(--brand-red); }
  .band { position: absolute; left: 0; right: 0; bottom: 0; height: 14px; display: flex; }
  .band__tech { flex: 1; background: var(--brand-blue); }
  .band__security { flex: 1; background: var(--brand-red); }
</style>
</head>
<body>
<main class="sheet">
  <section class="card card--back" aria-label="Card back">
    <div class="wordmark"><span>Hudson Crest IT Service</span><span class="wordmark__dot"></span></div>
    <div class="services">
      <p class="services__heading services__heading--tech">Technology:</p>
      <p>Computer, Network, Phone System, Copier, TV, Cabling</p>
      <p class="services__heading services__heading--security">Security:</p>
      <p>Video Surveillance, Access Control, Intercom, Fire Alarm, Burglar Alarm, Time Clock</p>
    </div>
  </section>

  <section class="card card--front" aria-label="Card front">
    <div class="wordmark"><span>Hudson Crest IT Service</span><span class="wordmark__dot"></span></div>
    <div class="holder">
      <p class="holder__name">Daniel Price</p>
      <p class="holder__role">Manager</p>
    </div>
    <div class="divider"></div>
    <div class="contact">
      <p class="contact__address">214 Harbor Avenue, Westfield,<br>NY 10457.</p>
      <p class="contact__row">
        <svg viewBox="0 0 24 24" aria-hidden="true"><path d="M6.6 10.8a15.1 15.1 0 0 0 6.6 6.6l2.2-2.2a1 1 0 0 1 1-.25 11.4 11.4 0 0 0 3.6.57 1 1 0 0 1 1 1V20a1 1 0 0 1-1 1A17 17 0 0 1 3 4a1 1 0 0 1 1-1h3.5a1 1 0 0 1 1 1c0 1.25.2 2.45.57 3.6a1 1 0 0 1-.25 1z"/></svg>
        +1 555 014 2270
      </p>
      <p class="contact__row">
        <svg viewBox="0 0 24 24" aria-hidden="true"><path d="M2 5h20v14H2zm2 2v.5l8 5 8-5V7l-8 5z"/></svg>
        hello@hudsoncrestit.com
      </p>
      <p class="contact__row">
        <svg viewBox="0 0 24 24" aria-hidden="true"><path d="M12 2a10 10 0 1 0 0 20 10 10 0 0 0 0-20zm6.9 9h-3a15 15 0 0 0-1.3-5.6A8 8 0 0 1 18.9 11zM12 4.1c.9 1.3 1.8 3.6 1.9 6.9h-3.8c.1-3.3 1-5.6 1.9-6.9zM9.4 5.4A15 15 0 0 0 8.1 11h-3a8 8 0 0 1 4.3-5.6zM5.1 13h3a15 15 0 0 0 1.3 5.6A8 8 0 0 1 5.1 13zm6.9 6.9c-.9-1.3-1.8-3.6-1.9-6.9h3.8c-.1 3.3-1 5.6-1.9 6.9zm2.6-1.3a15 15 0 0 0 1.3-5.6h3a8 8 0 0 1-4.3 5.6z"/></svg>
        www.hudsoncrestit.com
      </p>
    </div>
    <div class="band"><span class="band__tech"></span><span class="band__security"></span></div>
  </section>
</main>
</body>
</html>
```